Advert for Newspaper
National Newspaper ad for vantor wellness week
Advert for Newspaper - Medical
Creative Brief
Medical
Medical Optometrists, offering services to all ages but in particular those over 40 years of age who are more likely to suffer from glaucoma
The advert has to be 201mm in width and 90mm high. This is a direct response advert so the key things are the benefits, and the cut price and Call now! Please design using Indesign or illustrator with the original files also sent as well as a pdf. It can be full colour. The text in the advert has to include: Do you want the ultimate glaucoma detection and monitoring? The first private glaucoma clinic with 24 hour pressure monitoring in the UK* 24 hour pressure monitoring Advanced KRTL nerve fibre layer scans Gold standard visual fields Award winning care Fairlow Optometrists - Winners of independent practice of the year Vantor Wellness Week Limited time special offer for the month of September** Normal Price £2500 Special limited time offer £600 Book your appointment Call Now on 01632 960418 www.pelmarcare.co.uk (for more information) Small print - *Using corneal dimensional change **For eligible glaucoma sufferers only ask for T’s & C’s

```html
<!DOCTYPE html>
<html lang="en">
<head>
<meta charset="utf-8">
<title>Fairlow Optometrists – Glaucoma Clinic Advert</title>
<link href="https://fonts.googleapis.com/css2?family=Open+Sans:ital,wght@0,400;0,600;0,700;1,400;1,600&display=swap" rel="stylesheet">
<style>
  :root {
    --page: #e6e6e8;
    --paper: #ffffff;
    --brand-blue: #2a67ad;
    --button-blue: #3f7fc4;
    --button-text: #ffffff;
    --ink: #4a4d52;
    --ink-soft: #7a7e84;
    --photo-light: #f2f4f7;
    --photo-mid: #d9dee5;
    --badge: #c9ced6;
  }
  * { box-sizing: border-box; margin: 0; padding: 0; }
  html, body { width: 1200px; height: 947px; overflow: hidden; }
  body {
    background: var(--page);
    font-family: "Open Sans", Arial, sans-serif;
    color: var(--ink);
    position: relative;
  }
  .advert {
    position: absolute;
    left: 40px; top: 223px;
    width: 1120px; height: 501px;
    background: var(--paper);
    overflow: hidden;
  }
  .advert__photo {
    position: absolute;
    left: 380px; top: 0; width: 740px; height: 501px;
    background: radial-gradient(ellipse at 30% 55%, var(--photo-mid) 0%, var(--photo-light) 45%, var(--paper) 80%);
  }
  .brand {
    position: absolute; left: 40px; top: 36px;
    display: flex; align-items: center; gap: 12px;
  }
  .brand__dot { width: 34px; height: 34px; border-radius: 50%; background: var(--brand-blue); }
  .brand__name { font-size: 30px; font-weight: 600; color: var(--brand-blue); line-height: 1.05; }
  .award {
    position: absolute; left: 40px; top: 122px;
    font-size: 22px; font-weight: 600; color: var(--brand-blue);
  }
  .offer {
    position: absolute; left: 40px; top: 168px; width: 520px;
    font-size: 18px; line-height: 1.4; color: var(--ink);
  }
  .offer__price { margin-top: 6px; }
  .offer__special { color: var(--brand-blue); font-weight: 700; font-size: 22px; }
  .badge {
    position: absolute; left: 40px; top: 330px;
    width: 78px; height: 96px; border-radius: 6px; background: var(--badge);
  }
  .cta { position: absolute; top: 310px; width: 190px; text-align: center; }
  .cta--call { left: 150px; }
  .cta--web { left: 370px; width: 220px; }
  .cta__label { font-size: 14px; color: var(--ink); line-height: 1.3; }
  .cta__button {
    margin-top: 8px; background: var(--button-blue); color: var(--button-text);
    border-radius: 10px; padding: 14px 8px; font-weight: 700; font-size: 20px;
  }
  .cta--web .cta__button { font-size: 15px; padding: 18px 8px; }
  .headline {
    position: absolute; left: 660px; top: 40px; width: 420px;
    font-size: 33px; line-height: 1.22; font-weight: 400; color: var(--ink);
  }
  .headline strong { color: var(--brand-blue); font-weight: 700; }
  .intro {
    position: absolute; left: 660px; top: 210px; width: 420px;
    font-size: 17px; line-height: 1.35; color: var(--brand-blue);
  }
  .benefits {
    position: absolute; left: 660px; top: 270px; width: 420px;
    list-style: none; font-size: 17px; line-height: 1.4; color: var(--ink);
  }
  .benefits li::before { content: "* "; color: var(--brand-blue); }
  .small-print {
    position: absolute; left: 660px; top: 440px; width: 430px;
    font-size: 11px; line-height: 1.4; color: var(--ink-soft);
  }
</style>
</head>
<body>
  <section class="advert">
    <div class="advert__photo" role="img" aria-label="Soft-focus photograph of an eye seen through a magnifying glass over the word glaucoma"></div>

    <div class="brand">
      <span class="brand__dot"></span>
      <span class="brand__name">Fairlow Optometrists</span>
    </div>

    <p class="award">Winners of independent practice of the year</p>

    <div class="offer">
      <p>Vantor Wellness Week Limited time special offer for the month of September**</p>
      <p class="offer__price">Normal Price £2500 Special limited time offer <span class="offer__special">£600</span></p>
    </div>

    <div class="badge" aria-hidden="true"></div>

    <div class="cta cta--call">
      <p class="cta__label">Book your appointment<br>Call Now</p>
      <p class="cta__button">01632 960418</p>
    </div>
    <div class="cta cta--web">
      <p class="cta__label">For more information<br>Visit</p>
      <p class="cta__button">www.pelmarcare.co.uk</p>
    </div>

    <h1 class="headline">Do you want the ultimate <strong>glaucoma</strong> detection and monitoring?</h1>

    <p class="intro">The first private glaucoma clinic with 24 hour pressure monitoring in the UK*</p>

    <ul class="benefits">
      <li>24 hour pressure monitoring</li>
      <li>Advanced KRTL nerve fibre layer scans</li>
      <li>Gold standard visual fields</li>
      <li>Award winning care</li>
    </ul>

    <p class="small-print">*Using corneal dimensional change<br>**For eligible glaucoma sufferers only ask for T’s &amp; C’s</p>
  </section>
</body>
</html>
```